Flyer Design

STERLING SHADES
ph:9361 4085
7/41 Pellow Street
Malaga, WA 6069
we need a flyer design for a part broshure part flyer asking for business. well astablished small business for 15years. we manufacture blinds to domestic and commercial. custom made and premium quality. very competitive, free measure and quote even on weekend, plus we offer free fitting to all area. can supply all type of blinds as in big companies. such as roller blinds, roman blinds, timber venetians, slimline venetians, panel glide, vertical blinds, timber shutters etc.

Target Market(s)

new home

Industry/Entity Type

Small Business

Requirements
Nice to have
• a few different type of blinds in partially or part of it may be...

```html
<!DOCTYPE html>
<html lang="en">
<head>
<meta charset="utf-8">
<title>Sterling Shades Flyer</title>
<link rel="stylesheet" href="https://fonts.googleapis.com/css2?family=Open+Sans:wght@400;600&family=Roboto+Condensed:wght@700&display=swap">
<style>
  :root {
    --red-deep: #6e0306;
    --red: #a0080c;
    --red-bright: #b8100f;
    --maroon: #341410;
    --gold: #f7b500;
    --gold-light: #ffe24a;
    --yellow-text: #f5e61c;
    --white: #ffffff;
    --offwhite: #ebebeb;
  }
  * { margin: 0; padding: 0; box-sizing: border-box; }
  html, body { width: 965px; height: 1200px; overflow: hidden; background: var(--red-deep); }
  .flyer { position: relative; width: 965px; height: 1200px; overflow: hidden; font-family: "Open Sans", sans-serif; color: var(--white); }
  .flyer-backdrop { position: absolute; inset: 0; }
  .brand-name { position: absolute; top: 38px; left: 0; width: 100%; text-align: center; font-family: "Open Sans", sans-serif; font-weight: 600; font-size: 94px; line-height: 1; color: var(--offwhite); text-shadow: 0 4px 6px rgba(0,0,0,.55); letter-spacing: 1px; }
  .phone { position: absolute; top: 160px; left: 0; width: 100%; text-align: center; font-family: "Roboto Condensed", sans-serif; font-weight: 700; font-size: 46px; letter-spacing: 2px; color: var(--white); }
  .intro { position: absolute; left: 0; width: 100%; text-align: center; }
  .address { top: 326px; font-size: 21px; font-weight: 600; color: var(--yellow-text); }
  .experience { top: 368px; font-family: "Roboto Condensed", sans-serif; font-weight: 700; font-size: 38px; }
  .pitch { top: 456px; font-size: 24px; line-height: 39px; color: var(--yellow-text); }
  .pitch p + p { margin-top: 6px; }
  .supply { top: 640px; font-family: "Roboto Condensed", sans-serif; font-weight: 700; font-size: 30px; line-height: 44px; }
  .blind-types { position: absolute; top: 808px; left: 50px; width: 880px; list-style: none; display: grid; grid-template-columns: 318px 272px 290px; row-gap: 8px; }
  .blind-types li { display: flex; align-items: center; gap: 14px; font-family: "Roboto Condensed", sans-serif; font-weight: 700; font-size: 24px; height: 28px; }
  .tick { width: 22px; height: 22px; flex: none; }
  .gallery { position: absolute; top: 932px; left: 53px; display: flex; gap: 17px; }
  .gallery-photo { height: 196px; border-radius: 10px; border: 2px solid #f3f3f3; box-shadow: 0 4px 10px rgba(0,0,0,.5); }
  .photo-window { width: 266px; background: linear-gradient(135deg, #d4a06a, #a8703f 55%, #c89260); }
  .photo-venetian { width: 230px; background: linear-gradient(90deg, #c9ccd0, #4a4d52 35%, #2a2c30 70%, #555); }
  .photo-room { width: 326px; background: linear-gradient(90deg, #4b3a2f, #8a6a4e 45%, #3a2c24 80%, #6a5a50); }
  .tagline { position: absolute; top: 1145px; left: 0; width: 100%; text-align: center; font-size: 30px; letter-spacing: 4px; color: var(--yellow-text); word-spacing: 8px; }
</style>
</head>
<body>
<main class="flyer">
  <svg class="flyer-backdrop" width="965" height="1200" viewBox="0 0 965 1200" aria-hidden="true">
    <defs>
      <radialGradient id="red-field" cx="50%" cy="40%" r="75%">
        <stop offset="0" stop-color="#b8100f"/>
        <stop offset="0.6" stop-color="#8a0508"/>
        <stop offset="1" stop-color="#5a0205"/>
      </radialGradient>
      <linearGradient id="gold-band" x1="0" y1="0" x2="1" y2="0">
        <stop offset="0" stop-color="#c24a00"/>
        <stop offset="0.35" stop-color="#ffd21a"/>
        <stop offset="0.65" stop-color="#ffe24a"/>
        <stop offset="1" stop-color="#d06a00"/>
      </linearGradient>
      <radialGradient id="maroon-field" cx="50%" cy="50%" r="60%">
        <stop offset="0" stop-color="#3a1611"/>
        <stop offset="1" stop-color="#2a0e0b"/>
      </radialGradient>
    </defs>
    <rect width="965" height="1200" fill="url(#red-field)"/>
    <!-- top swoosh -->
    <path d="M0 345 Q480 190 965 330 L965 370 Q480 260 0 375 Z" fill="#c00f10" opacity=".8"/>
    <path d="M0 330 Q480 225 965 345 L965 372 Q480 262 0 372 Z" fill="url(#gold-band)"/>
    <!-- dark centre field -->
    <path d="M0 368 Q480 262 965 370 L965 660 Q480 800 0 660 Z" fill="url(#maroon-field)"/>
    <path d="M0 370 Q480 268 965 372" fill="none" stroke="#ffe68a" stroke-width="2"/>
    <!-- bottom swoosh -->
    <path d="M0 655 Q480 800 965 660 L965 700 Q480 810 0 690 Z" fill="url(#gold-band)"/>
    <path d="M0 685 Q480 805 965 695 L965 735 Q480 830 0 720 Z" fill="#c2100f" opacity=".85"/>
    <path d="M0 660 Q480 798 965 664" fill="none" stroke="#fff2a0" stroke-width="2"/>
  </svg>

  <h1 class="brand-name">STERLING SHADES</h1>
  <p class="phone">Ph: 9361 4085</p>

  <p class="intro address">7/41 Pellow Street, Malaga, WA 6069</p>
  <h2 class="intro experience">15 Years of Experience</h2>
  <div class="intro pitch">
    <p>We manufacture blinds to domestic and commercial.<br>Custom made and premium quality.</p>
    <p>Very competitive, free measure and quote even on weekend,<br>plus we offer free fitting to all area.</p>
  </div>
  <p class="intro supply">Can supply all type of blinds as in<br>big companies</p>

  <ul class="blind-types">
    <li><svg class="tick" viewBox="0 0 22 22"><circle cx="11" cy="11" r="10" fill="#f4f4f4"/><path d="M6 11.5l3.5 3.5L16.5 7" fill="none" stroke="#e6b800" stroke-width="3" stroke-linecap="round"/></svg>Roller Blinds</li>
    <li><svg class="tick" viewBox="0 0 22 22"><circle cx="11" cy="11" r="10" fill="#f4f4f4"/><path d="M6 11.5l3.5 3.5L16.5 7" fill="none" stroke="#e6b800" stroke-width="3" stroke-linecap="round"/></svg>Roman Blinds</li>
    <li><svg class="tick" viewBox="0 0 22 22"><circle cx="11" cy="11" r="10" fill="#f4f4f4"/><path d="M6 11.5l3.5 3.5L16.5 7" fill="none" stroke="#d01818" stroke-width="3" stroke-linecap="round"/></svg>Timber Venetians</li>
    <li><svg class="tick" viewBox="0 0 22 22"><circle cx="11" cy="11" r="10" fill="#f4f4f4"/><path d="M6 11.5l3.5 3.5L16.5 7" fill="none" stroke="#e6b800" stroke-width="3" stroke-linecap="round"/></svg>Slimline Venetians</li>
    <li><svg class="tick" viewBox="0 0 22 22"><circle cx="11" cy="11" r="10" fill="#f4f4f4"/><path d="M6 11.5l3.5 3.5L16.5 7" fill="none" stroke="#e6b800" stroke-width="3" stroke-linecap="round"/></svg>Panel Glide</li>
    <li><svg class="tick" viewBox="0 0 22 22"><circle cx="11" cy="11" r="10" fill="#f4f4f4"/><path d="M6 11.5l3.5 3.5L16.5 7" fill="none" stroke="#d01818" stroke-width="3" stroke-linecap="round"/></svg>Vertical Blinds</li>
    <li><svg class="tick" viewBox="0 0 22 22"><circle cx="11" cy="11" r="10" fill="#f4f4f4"/><path d="M6 11.5l3.5 3.5L16.5 7" fill="none" stroke="#e6b800" stroke-width="3" stroke-linecap="round"/></svg>Timber Shutters etc.</li>
  </ul>

  <div class="gallery">
    <div class="gallery-photo photo-window" role="img" aria-label="Photo of a timber-framed window with a blind"></div>
    <div class="gallery-photo photo-venetian" role="img" aria-label="Close-up photo of dark slimline venetian blinds beside a window handle"></div>
    <div class="gallery-photo photo-room" role="img" aria-label="Photo of a room with timber venetian blinds and striped chairs"></div>
  </div>

  <p class="tagline">MODERN, STYLISH, PEACEFUL</p>
</main>
</body>
</html>
```